Coffee Cocktails Recipe Flips cards

create (12) recipe cards that illustrate the finished beverage, with its description, ingredients, and instructions. each card should be 5"x7" and styled to incorporate brand theme and the cultural elements of the beverage. cards will be used for stuffers in shipments of product, used by bartenders, and digitally shared. Present each drink in glassware that embodies the spirit of the culture it represents, garnishing with flair and a nod to the exotic origins, creating a multisensory experience that'll transport the drinker to distant lands with just one indulgent sip.
The presentation of each drink should reflect the cultural fusion aesthetically, using suggested glassware and garnishes to bring the exotic themes to life. Enjoy crafting these drinks and take your guests on a flavorful voyage around the world with each sip!

Target Market(s)

Consumers and Bars and Restaurants

Industry/Entity Type

coffee and adult beverages

Colors

Designer to choose colors to be used in the design.

Requirements
Must have
• brand alignment, styled to reflect the uniqueness of each recipe
Should not have
• appropriate glassware, garnishments, and images of raw ingredients

```html
<!DOCTYPE html>
<html lang="en">
<head>
<meta charset="utf-8">
<title>Café Mocha Bliss — Recipe Card</title>
<link href="https://fonts.googleapis.com/css2?family=Comfortaa:wght@700&family=Lexend:wght@600&family=Source+Sans+3:ital,wght@0,400;1,700&display=swap" rel="stylesheet">
<style>
  :root {
    --stage: #cfcfcf;
    --paper: #ffffff;
    --ink: #2b2b2b;
    --teal-deep: #1b3a44;
    --teal-mid: #2d6660;
    --green-soft: #5fa383;
    --photo-light: #e6ddd2;
    --photo-dark: #a88f78;
  }
  * { margin: 0; padding: 0; box-sizing: border-box; }
  html, body { width: 1200px; height: 1200px; overflow: hidden; }
  body {
    background: var(--stage);
    font-family: "Source Sans 3", "Helvetica Neue", Arial, sans-serif;
    color: var(--ink);
  }
  .recipe-card {
    position: absolute;
    left: 230px; top: 83px;
    width: 740px; height: 1034px;
    background: var(--paper);
    overflow: hidden;
  }
  .card-art { position: absolute; inset: 0; width: 740px; height: 1034px; }
  .brand-mark {
    position: absolute;
    left: 580px; top: 43px;
    width: 112px; height: 112px;
    border-radius: 50%;
    background: var(--paper);
    border: 2px solid var(--teal-deep);
    display: flex; align-items: center; justify-content: center;
    font-family: "Lexend", "Helvetica Neue", Arial, sans-serif;
    font-weight: 600; font-size: 30px;
    color: var(--teal-mid);
  }
  .title-cafe { position: absolute; left: 40px; top: 110px; width: 420px; height: 150px; }
  .title-drink {
    position: absolute; left: 54px; top: 262px;
    font-family: "Lexend", "Helvetica Neue", Arial, sans-serif;
    font-weight: 600; font-size: 66px; line-height: 1;
    color: #111;
    letter-spacing: 0.5px;
  }
  .description {
    position: absolute; left: 55px; top: 352px; width: 660px;
    font-size: 17.6px; line-height: 24.4px;
  }
  .section-label {
    position: absolute; left: 0; width: 226px; height: 30px;
    background: linear-gradient(90deg, var(--teal-deep), var(--green-soft));
    color: #fff;
    font-style: italic; font-weight: 700; font-size: 20px;
    line-height: 30px; padding-left: 51px;
    letter-spacing: 0.3px;
  }
  .label-ingredients { top: 535px; }
  .label-instructions { top: 766px; }
  .ingredient-list {
    position: absolute; left: 57px; top: 576px;
    list-style: none; font-size: 17.6px; line-height: 24.4px;
  }
  .ingredient-list li::before { content: "• "; }
  .instruction-list {
    position: absolute; left: 68px; top: 807px; width: 420px;
    font-size: 17.6px; line-height: 24.4px;
    padding-left: 0; list-style-position: outside; margin-left: 0;
  }
  .instruction-list li { margin-left: 0; padding-left: 2px; }
</style>
</head>
<body>
  <article class="recipe-card">
    <svg class="card-art" viewBox="0 0 740 1034" xmlns="http://www.w3.org/2000/svg">
      <defs>
        <linearGradient id="waveTop" x1="0" y1="0" x2="1" y2="0.3">
          <stop offset="0" stop-color="#1b3a44"/>
          <stop offset="1" stop-color="#5fa383"/>
        </linearGradient>
        <linearGradient id="waveSide" x1="0" y1="0" x2="0.3" y2="1">
          <stop offset="0" stop-color="#1b3a44"/>
          <stop offset="1" stop-color="#5fa383"/>
        </linearGradient>
        <linearGradient id="photoTone" x1="0" y1="0" x2="1" y2="1">
          <stop offset="0" stop-color="#e6ddd2"/>
          <stop offset="0.6" stop-color="#cdbba8"/>
          <stop offset="1" stop-color="#a88f78"/>
        </linearGradient>
      </defs>
      <path class="wave-top" fill="url(#waveTop)"
        d="M170 0 L740 0 L740 225 C690 205 640 222 560 212 C470 200 440 130 360 112 C280 94 250 0 170 0 Z"/>
      <path class="wave-top-inset" fill="#ffffff"
        d="M390 0 C400 60 470 72 520 112 C575 160 650 175 705 132 C745 100 722 40 740 18 L740 0 Z"/>
      <path class="wave-side" fill="url(#waveSide)"
        d="M740 470 C690 482 655 525 668 600 C680 680 640 722 580 762 C520 805 500 885 530 960 C546 1000 560 1034 560 1034 L740 1034 Z"/>
      <g role="img" aria-label="Photo of a cup of black coffee with a jug of milk, scattered coffee beans and cinnamon sticks on marble">
        <path fill="url(#photoTone)" stroke="#ffffff" stroke-width="5"
          d="M355 570 C372 525 440 522 500 532 C560 542 622 522 652 562 C684 612 664 702 622 760 C580 812 470 804 420 784 C368 762 338 700 348 640 Z"/>
      </g>
    </svg>

    <div class="brand-mark">K&amp;T</div>

    <svg class="title-cafe" viewBox="0 0 420 150" xmlns="http://www.w3.org/2000/svg">
      <defs>
        <linearGradient id="cafeFill" x1="0" y1="0" x2="1" y2="0">
          <stop offset="0" stop-color="#1b3a44"/>
          <stop offset="0.6" stop-color="#2d6660"/>
          <stop offset="1" stop-color="#6fb890"/>
        </linearGradient>
      </defs>
      <text x="8" y="126" font-family="Comfortaa, 'Helvetica Neue', Arial, sans-serif" font-weight="700" font-size="148"
        fill="url(#cafeFill)" stroke="#1b2f33" stroke-width="3" paint-order="stroke">Café</text>
    </svg>

    <h1 class="title-drink">Mocha Bliss</h1>

    <p class="description">Indulge in the balance of bittersweet espresso entwined with rich chocolate syrup to enjoy the luxe texture of the Café Mocha Bliss. Gently pour the espresso into your favorite mug, caress it with the velvety touch of chocolate, and crown the mix with steamed milk as soft as clouds. End with a swirl of whipped cream, graced with a sprinkling of chocolate shavings or a delicate dusting of cocoa powder—your canvas of comfort.</p>

    <h2 class="section-label label-ingredients">INGREDIENTS:</h2>
    <ul class="ingredient-list">
      <li>5g K&amp;T Classic Black Coffee</li>
      <li>8oz hot water</li>
      <li>2 tablespoons chocolate syrup</li>
      <li>Steamed milk</li>
      <li>Whipped cream</li>
      <li>Chocolate shavings for garnish</li>
    </ul>

    <h2 class="section-label label-instructions">Instructions:</h2>
    <ol class="instruction-list">
      <li>Mix 8oz of hot water with one packet K&amp;T Classic Black Instant Coffee, mix well until powder is fully dissolved.</li>
      <li>Pour the Coffee into a mug.</li>
      <li>Stir in the chocolate syrup until well combined.</li>
      <li>Top with steamed milk.</li>
      <li>Add a generous dollop of whipped cream.</li>
      <li>Garnish with chocolate shavings.</li>
    </ol>
  </article>
</body>
</html>
```